依頼詳細
いまあるサンプルを春らしく変えて頂いても結構ですし、違うイメージで一から作成して頂いても結構です。このサンプルデザインに特にこだわりがあるわけではありませんので、良いデザインがあればどんどんご提案下さい。

対象が女性の50代~70代になるのでデザインのおしゃれさも大事ですが、シンプルでわかりやすいデザインを希望します。

A3サイズとB4サイズで作成をして下さい。
内容はまったく同じで用紙に合わせてレイアウトを調整して下さい。

真ん中部分の広告商品の商品名や価格はダミーで入れて頂ければ後から私が加筆します。

今後は季節ごとに配色を変えたり、季節感のある物を軽く挿入する程度で、作って頂いたデザインを通年使用していく予定です。

2ヶ月ごとに新聞広告の作成がありますので、今後ともよろしくお願いします。

選択させて頂いた広告の著作権(財産権)等は当方に譲渡をお願いします。フォントや画像素材などを利用する場合は上記利用用途に使用できることを確認し、第三者の知的財産権等に注意して下さい。
記載項目
会期 4月5日(火)~10日(日)

営業時間 10:00~18:00(最終日のみ15:00迄)

会場 アサギリモール一階・北側 SPACEはなゆき 京都市北区雲井南梅枝町38-6

主催 株式会社明葉 京都市北区雲井西竹丘町17-42 tel075-555-0183

2015年4月のサンプルにあるネットショップとブログの案内は省いて下さい。
サイズ
A3
ページ数
片面
希望イメージ
シンプル 複雑
単色 カラフル
暗い 明るい
日常 高級
遊び心 厳粛
未来的 伝統的
女性的 男性的
希望する色
納品ファイル
• 高解像度JPG (.jpg)
• イラストレーター形式 (.ai)
• フォトショップ形式 (.psd)
補足説明
サンプルを添付をさせて頂きます
たくさんのすばらしいデザインを作成して頂き、皆様本当にありがとうございます。

良いデザインばかりなので選定作業が困難を極めています(笑)

採用させて頂いた方はもちろん、それ以外の方も今後ともよろしくお願い申し上げます。

ありがとうございました。
■ 選んだ理由

女性のデザイナーさんらしくやさしさが伝わってきました。

■ 提案者全員のお礼・コメント

皆様本当にありがとうございました。明葉の広告をこんなたくさんの方にデザインしていただきうれしく思います。今後もよろしくお願いします。

```html
<!DOCTYPE html>
<html lang="ja">
<head>
<meta charset="utf-8">
<title>明葉の婦人服 春祭り</title>
<link href="https://fonts.googleapis.com/css2?family=Shippori+Mincho+B1:wght@800&family=Noto+Sans+JP:wght@400;700;900&family=Noto+Serif+JP:wght@700;900&display=swap" rel="stylesheet">
<style>
:root{
  --bg-top:#fde3ea;
  --bg-mid:#fbe9ef;
  --bg-low:#f8dfe6;
  --title-red:#d8143c;
  --accent-red:#e2183e;
  --ink:#222;
  --gold:#c9a24a;
  --tag-pink:#e86b93;
  --tag-green:#7cc043;
  --tag-orange:#f39b2f;
  --tag-purple:#9b6bc1;
  --tag-blue:#3fa6d9;
  --tag-red:#e33b4f;
  --summer:#f39a1e;
  --spring:#ea5f8d;
}
*{margin:0;padding:0;box-sizing:border-box}
html,body{width:849px;height:1200px;overflow:hidden}
body{font-family:"Noto Sans JP",sans-serif;color:var(--ink)}
.flyer{position:relative;width:849px;height:1200px;overflow:hidden;
  background:linear-gradient(180deg,var(--bg-top) 0%,#fff4f7 45%,var(--bg-mid) 70%,var(--bg-low) 100%)}
.blossom{position:absolute;border-radius:50%;
  background:radial-gradient(circle,#f7b9cb 0%,#fbd5e0 45%,rgba(251,213,224,0) 72%)}
.blossom.top{left:560px;top:-60px;width:360px;height:360px}
.blossom.right{left:640px;top:300px;width:260px;height:260px;opacity:.7}
.blossom.bottom{left:460px;top:960px;width:460px;height:330px}
.brand{position:absolute;left:22px;top:14px;color:var(--gold)}
.brand-name{font-family:"Noto Serif JP",serif;font-weight:700;font-size:30px;letter-spacing:3px;display:flex;align-items:center;gap:8px}
.brand-name::before{content:"";width:14px;height:14px;border-radius:50%;background:var(--gold)}
.brand-sub{font-family:"Noto Serif JP",serif;font-weight:700;font-size:17px;margin-left:22px}
.brand-sub span{font-size:12px}
.festival-lettering{position:absolute;left:530px;top:10px;width:300px;height:380px;border-radius:40px;
  background:linear-gradient(160deg,rgba(236,110,150,.55),rgba(244,160,185,.35))}
.title{position:absolute;left:350px;top:55px;writing-mode:vertical-rl;
  font-family:"Shippori Mincho B1",serif;font-weight:800;font-size:134px;line-height:1;letter-spacing:-4px;
  color:var(--title-red);
  text-shadow:0 0 6px #fff,3px 3px 0 #fff,-3px -3px 0 #fff,3px -3px 0 #fff,-3px 3px 0 #fff,0 4px 0 #fff,4px 0 0 #fff}
.items{position:absolute;left:18px;top:112px;width:310px;list-style:none}
.item{height:106px;padding-top:8px}
.tag{display:inline-block;min-width:260px;padding:3px 12px;font-size:15px;font-weight:700;color:#fff;border-radius:0 20px 20px 0}
.price{font-weight:900;font-size:56px;line-height:1.05;color:var(--title-red);margin-top:4px;white-space:nowrap}
.price small{font-size:26px;font-weight:900}
.price .tax{font-size:17px;font-weight:700}
.tag.pink{background:var(--tag-pink)}.tag.green{background:var(--tag-green)}.tag.orange{background:var(--tag-orange)}
.tag.purple{background:var(--tag-purple)}.tag.blue{background:var(--tag-blue)}.tag.red{background:var(--tag-red)}
.venue{position:absolute;left:18px;top:764px;display:flex;align-items:center;gap:12px}
.venue-mark{width:52px;height:52px;border-radius:50%;background:var(--gold);color:#fff;font-size:15px;font-weight:700;display:flex;align-items:center;justify-content:center}
.venue-name{font-family:"Noto Serif JP",serif;font-weight:900;font-size:30px;white-space:nowrap}
.venue-address{position:absolute;left:18px;top:828px;font-size:11px;line-height:1.5;white-space:nowrap}
.map{position:absolute;left:18px;top:868px;width:310px;height:300px;background:linear-gradient(180deg,#ffffff,#f1eef0);border:1px solid #d9c9cf}
.seasons{position:absolute;left:560px;top:405px;display:flex;gap:14px}
.season{width:96px;height:96px;border-radius:50%;color:#fff;font-family:"Noto Serif JP",serif;font-weight:900;font-size:32px;display:flex;align-items:center;justify-content:center}
.season.summer{background:var(--summer);margin-top:30px}
.season.spring{background:var(--spring)}
.special{position:absolute;left:515px;top:536px;font-family:"Noto Serif JP",serif;font-weight:900;font-size:56px;color:var(--accent-red);letter-spacing:-1px;white-space:nowrap}
.pledge{position:absolute;left:585px;top:624px;font-size:14px;line-height:1.6;font-weight:700;white-space:nowrap}
.bargain{position:absolute;left:556px;top:700px;font-size:25px;font-weight:900;color:var(--accent-red);border-bottom:3px solid var(--accent-red);padding-bottom:2px;white-space:nowrap}
.dates{position:absolute;right:22px;top:752px;font-weight:900;color:var(--accent-red);font-size:58px;line-height:1;display:flex;align-items:flex-end;white-space:nowrap}
.dates .dow{display:inline-flex;align-items:center;justify-content:center;width:24px;height:24px;border-radius:50%;background:var(--accent-red);color:#fff;font-size:14px;margin:0 4px 6px}
.dates .tilde{font-size:44px;margin:0 2px}
.hours{position:absolute;left:520px;top:828px;font-size:15px;font-weight:700;white-space:nowrap}
.organizer{position:absolute;left:560px;top:878px;font-size:13px;line-height:1.55;font-style:normal}
.organizer .company{font-family:"Noto Serif JP",serif;font-size:18px;font-weight:900}
.organizer .company b{font-size:30px;margin-left:4px}
</style>
</head>
<body>
<div class="flyer">
  <div class="blossom top" role="img" aria-label="桜の花のイラスト"></div>
  <div class="blossom right" role="img" aria-label="桜の花のイラスト"></div>
  <div class="blossom bottom" role="img" aria-label="桜の枝のイラスト"></div>

  <header class="brand">
    <div class="brand-name">CORALINE</div>
    <div class="brand-sub">Meiyo Co.,Ltd. <span>コラリン</span></div>
  </header>

  <div class="festival-lettering" role="img" aria-label="筆文字「春祭り」"></div>

  <h1 class="title">明葉の婦人服</h1>

  <ul class="items">
    <li class="item"><span class="tag pink">シルクスカーフ・ネックカバー各種</span><p class="price">1,000<small>円〜</small><span class="tax">（税込）</span></p></li>
    <li class="item"><span class="tag green">綿ツイルシャツ各種（日本製）</span><p class="price">2,900<small>円〜</small><span class="tax">（税込）</span></p></li>
    <li class="item"><span class="tag orange">チュニック各種（S〜LL）</span><p class="price">2,900<small>円〜</small><span class="tax">（税込）</span></p></li>
    <li class="item"><span class="tag purple">カーディガン各種（日本製）</span><p class="price">4,900<small>円〜</small><span class="tax">（税込）</span></p></li>
    <li class="item"><span class="tag blue">パンツ各種（S〜3L）</span><p class="price">3,900<small>円〜</small><span class="tax">（税込）</span></p></li>
    <li class="item"><span class="tag red">ジャケット各種</span><p class="price">5,900<small>円〜</small><span class="tax">（税込）</span></p></li>
  </ul>

  <div class="venue"><span class="venue-mark">会場</span><span class="venue-name">SPACEはなゆき</span></div>
  <p class="venue-address">アサギリモール一階・北側　京都市北区雲井南梅枝町38-6</p>
  <div class="map" role="img" aria-label="会場周辺の案内地図"></div>

  <div class="seasons"><span class="season summer">夏物</span><span class="season spring">春物</span></div>
  <p class="special">特別価格!</p>
  <p class="pledge">品質・価格に自信を持って<br>取り揃えております。ご期待ください!</p>
  <p class="bargain">今回もお値打ち品多数</p>

  <p class="dates">4/5<span class="dow">火</span><span class="tilde">〜</span>4/10<span class="dow">日</span></p>
  <p class="hours">10:00〜18:00（最終日のみ15:00迄）</p>

  <address class="organizer">
    <div class="company">主催者:株式会社<b>明葉</b></div>
    京都市北区雲井西竹丘町17-42<br>
    tel075-555-0183<br>
    www.e-meiyo.com
  </address>
</div>
</body>
</html>
```